UK Based Internet hosting Company wants a vibrant eCommerce site designed.

We have only just had our logo and brand designed by Pixel Forum which went so well that we would like to open up our website design project on here too.

The company is called 'Quay Server Lantern' and we provide a range of website hosting, dedicated server, domain name and email solutions that people will be able to purchase online in neatly packaged options from the outset.

Our logo and brand is bright turquoise, black & white (samples of branding will be attached with this project) but we would like the website to be very vibrant with good use of white space rather than a black website.

We want to appeal to end users so web designers, developers and people who would like to host their website. But we also want to appeal to resellers that would like to resell our hosting packages too.

We want a big push on social media and blogging on the site as we would like our brand to be 100% up with Chatterleaf, Murmel, workLoop, Vidplume and Zorbix+. It would be great to have this integrated into the site with share buttons and rating buttons etc.

We would like to see a homepage initially with a view to providing several page layers down to help our in-house developers hook in our back-end into this front end effectively.

Great customer experience and an easy to navigate journey to the checkout when purchasing the hosting packages is paramount !!

We like how the following sites are set-out and presented:

www.brightmarrow.uk
http://www.tallyfold.co.uk
https://www.qv7.net/web-hosting/

Target Market(s)

We have 3 target markets.

Target market 1 - end users, consumers such as Web Designers, Developers and small businesses.

Target Market 2 - Resellers, small businesses that would like to resell our services.

Target Market 3 - Medium to large businesses that would like more of a bespoke solution.

Industry/Entity Type

Internet

Requirements
Must have
• Colourful, bright, bold, easy to navigate and to purchase packages.
• Plenty of call to actions, social media, ratings.
• Video case studies and testimonials would be nice.

```html
<!DOCTYPE html>
<html lang="en">
<head>
<meta charset="utf-8">
<title>Quay Server Lantern – Hosting</title>
<link href="https://fonts.googleapis.com/css2?family=Open+Sans:wght@400;600;700&display=swap" rel="stylesheet">
<style>
:root{
  --teal:#2dbdbf;
  --teal-dark:#22a3a5;
  --navy:#2c3e50;
  --navy-deep:#253444;
  --grey-bg:#ececec;
  --white:#ffffff;
  --text:#333b44;
  --muted:#6f7780;
  --line:#d8dbde;
}
*{box-sizing:border-box;margin:0;padding:0}
html,body{width:1200px;height:2802px;overflow:hidden}
body{font-family:"Open Sans",Arial,sans-serif;color:var(--text);background:var(--white);position:relative;font-size:12px}
.abs{position:absolute}
/* header */
.site-header{top:0;left:0;width:1200px;height:65px;background:var(--white);border-bottom:1px solid var(--line)}
.brand{left:245px;top:14px;display:flex;align-items:center;gap:9px}
.brand-dot{width:34px;height:34px;border-radius:50%;background:var(--teal)}
.brand-name{font-weight:700;font-size:16px;color:var(--navy);width:120px;line-height:17px}
.main-nav{left:415px;top:0;display:flex;height:65px}
.main-nav a{display:flex;align-items:center;padding:0 7px;font-size:9px;font-weight:600;color:var(--navy);text-decoration:none;text-transform:uppercase;white-space:nowrap}
.main-nav a + a{margin-left:6px}
.main-nav a.active{background:var(--teal);color:var(--white)}
.top-links{right:210px;top:6px;display:flex;gap:3px}
.top-links span{background:var(--teal);color:var(--white);font-size:8px;padding:2px 7px;text-transform:uppercase}
.call-us{right:210px;top:32px;font-size:9px;font-weight:700;color:var(--navy);white-space:nowrap}
.call-us b{color:#e0433b}
/* hero */
.hero{top:65px;left:0;width:1200px;height:402px;background:radial-gradient(ellipse at 50% 40%,#5c84ad 0%,#2c4f78 45%,#142742 100%)}
.hero-arrow{width:30px;height:30px;background:var(--teal);top:222px;display:flex;align-items:center;justify-content:center}
.search-bar{top:380px;left:280px;width:612px;height:34px;background:rgba(255,255,255,.92);display:flex}
.search-bar .www{width:62px;background:#3a4552;color:var(--white);display:flex;align-items:center;justify-content:center;font-size:11px}
.search-bar .field{flex:1;padding:0 10px;display:flex;align-items:center;color:var(--muted);font-size:12px}
.search-bar .go{width:34px;display:flex;align-items:center;justify-content:center}
/* features */
.features{top:467px;left:0;width:1200px;height:140px;background:var(--white)}
.feature{top:32px;width:190px;display:flex;gap:10px}
.feature h4{font-size:13px;font-weight:600;color:var(--navy);margin-bottom:3px}
.feature p{font-size:9.5px;color:var(--muted);line-height:12px}
/* grey zones */
.zone-grey{left:0;width:1200px;background:var(--grey-bg)}
.bar{left:210px;width:780px;height:36px;display:flex;align-items:center;padding-left:22px;font-weight:700;font-size:14px;color:var(--white);text-transform:uppercase;border-left:5px solid var(--teal-dark)}
.bar.teal{background:var(--teal)}
.bar.navy{background:var(--navy);border-left-color:var(--teal)}
.bar .ctrl{position:absolute;right:10px;top:9px;width:18px;height:18px;background:rgba(255,255,255,.3)}
.bar .pair{position:absolute;right:10px;top:9px;display:flex;gap:3px}
.bar .pair i{width:16px;height:18px;background:rgba(255,255,255,.3);display:block}
.col h3{font-size:16px;font-weight:700;color:var(--navy);margin-bottom:14px}
.col p{font-size:10px;line-height:14px;color:var(--muted)}
.ticks li{list-style:none;font-size:10px;color:var(--muted);line-height:17px;padding-left:14px;position:relative}
.ticks li:before{content:"";position:absolute;left:0;top:6px;border-left:5px solid var(--teal);border-top:3px solid transparent;border-bottom:3px solid transparent}
.quote-box{background:var(--white);padding:14px 16px;font-size:10px;line-height:14px;color:var(--muted)}
.team-card{top:929px;width:172px;height:220px;background:var(--white)}
.team-photo{width:162px;height:166px;margin:5px}
.team-card h5{text-align:center;font-size:13px;font-weight:600;color:var(--navy);margin-top:8px}
.team-card small{display:block;text-align:center;font-size:9px;color:var(--muted)}
/* services */
.service{top:1286px;width:120px;text-align:center}
.service h5{font-size:13px;font-weight:600;color:var(--navy);margin:10px 0 6px}
.service p{font-size:9.5px;line-height:12px;color:var(--muted)}
.tabs{top:1452px;left:210px;display:flex;gap:3px}
.tabs span{font-size:11px;padding:5px 10px;background:#e4e6e8;color:var(--navy);text-transform:uppercase}
.tabs span.on{background:var(--white);color:var(--teal)}
.tab-body{top:1478px;left:210px;width:780px;height:133px;background:var(--white);border:1px solid var(--line);padding:12px 14px;font-size:9.5px;line-height:14px;color:var(--muted);overflow:hidden}
/* pricing */
.plan{top:1723px;width:187px;height:267px;background:#f5f6f7}
.plan-head{height:33px;background:var(--navy);color:var(--white);font-size:12px;padding:9px 12px}
.plan.featured .plan-head,.plan.featured .plan-btn{background:var(--teal)}
.plan-price{font-size:21px;color:var(--navy);padding:12px 12px 8px;font-weight:600}
.plan-price small{font-size:14px;font-weight:400}
.plan ul{padding:6px 12px}
.plan li{list-style:none;font-size:9.5px;color:var(--muted);line-height:34px;display:flex;align-items:center;gap:6px}
.plan.featured li{color:var(--teal)}
.plan li i{width:10px;height:10px;border:1px solid var(--muted);display:inline-block}
.plan-btn{position:absolute;bottom:0;left:0;width:100%;height:34px;background:var(--navy);color:var(--white);font-size:12px;font-weight:600;display:flex;align-items:center;justify-content:center;text-transform:uppercase}
.newsletter{top:2020px;left:210px;width:780px;height:100px;background:var(--white)}
/* map & contact */
.map{top:2153px;left:0;width:1200px;height:334px;background:linear-gradient(135deg,#ece6c8 0%,#f3efd8 40%,#e8e2c2 70%,#dcdcd0 100%)}
.field-box{background:var(--white);border:1px solid var(--line);height:24px;font-size:10px;color:var(--muted);padding:4px 8px}
.send{background:var(--teal);color:var(--white);font-size:15px;font-weight:600;display:flex;align-items:center;justify-content:center}
.addr p{font-size:10px;line-height:14px;color:var(--muted);display:flex;gap:8px;align-items:center}
.site-footer{top:2767px;left:0;width:1200px;height:35px;background:var(--navy-deep);color:#c7cdd3;font-size:10px;display:flex;align-items:center;justify-content:center}
</style>
</head>
<body>

<header class="abs site-header">
  <div class="abs brand"><span class="brand-dot"></span><span class="brand-name">Quay Server Lantern</span></div>
  <nav class="abs main-nav">
    <a class="active" href="#">Domain Names</a><a href="#">Web Hosting</a><a href="#">Reseller Hosting</a><a href="#">Servers</a><a href="#">E-mail</a>
  </nav>
  <div class="abs top-links"><span>Login</span><span>Register</span><span>Support</span></div>
  <div class="abs call-us">CALL US NOW: <b>555-210-4417</b></div>
</header>

<section class="abs hero" role="img" aria-label="Photo of a person relaxing, hands behind head, in front of a glowing world network map">
  <div class="abs hero-arrow" style="left:0"><svg width="10" height="12"><path d="M8 1 2 6l6 5" stroke="#fff" stroke-width="2" fill="none"/></svg></div>
  <div class="abs hero-arrow" style="right:0"><svg width="10" height="12"><path d="M2 1l6 5-6 5" stroke="#fff" stroke-width="2" fill="none"/></svg></div>
</section>
<div class="abs search-bar"><div class="www">WWW</div><div class="field">search your domain name....</div><div class="go"><svg width="14" height="14"><circle cx="6" cy="6" r="4.5" stroke="#555" stroke-width="2" fill="none"/><path d="M9.5 9.5 13 13" stroke="#555" stroke-width="2"/></svg></div></div>

<section class="abs features">
  <div class="abs feature" style="left:205px"><svg width="20" height="18"><path d="M10 1 19 17H1z" fill="#3a4552"/></svg><div><h4>New way of vision</h4><p>Curabitur at rhoncus quam. In in tortor quis sem tempor ultricies in.</p></div></div>
  <div class="abs feature" style="left:420px"><svg width="18" height="18"><path d="M2 16C2 6 8 2 16 2c0 8-4 14-14 14z" fill="#3a4552"/></svg><div><h4>Fresh ideas</h4><p>Suspendisse auctor sagittis quam quis rhoncus.</p></div></div>
  <div class="abs feature" style="left:619px"><svg width="18" height="18"><path d="M9 1 17 8h-2v9H3V8H1z" fill="#3a4552"/></svg><div><h4>Strong foundations</h4><p>Curabitur at rhoncus quam. In in tortor quis sem tempor ultricies in.</p></div></div>
  <div class="abs feature" style="left:818px"><svg width="22" height="18"><circle cx="7" cy="5" r="4" fill="#3a4552"/><circle cx="16" cy="5" r="4" fill="#3a4552"/><path d="M0 17c0-6 14-6 14 0zM9 17c0-6 13-6 13 0z" fill="#3a4552"/></svg><div><h4>Great support</h4><p>Suspendisse auctor sagittis quam quis rhoncus.</p></div></div>
</section>

<div class="abs zone-grey" style="top:607px;height:595px"></div>
<div class="abs bar teal" style="top:612px">About us<span class="ctrl"></span></div>
<div class="abs col" style="left:210px;top:680px;width:245px"><h3>Who We Are?</h3><p>Suspendisse dictum quam tortor, et dapibus lacus. Quisque euismod lacus in mi consequat sed pulvinar elit ultricies. Nam eu ligula ut massa lobortis scelerisque. Curabitur at rhoncus quam. In in tortor quis sem tempor ultricies in eu risus. Fusce posuere justo et metus semper molestie.</p></div>
<div class="abs col" style="left:483px;top:680px;width:230px"><h3>Why us?</h3><ul class="ticks"><li>Suspendisse dictum quam tortor</li><li>Sed dapibus lacus.</li><li>Quisque euismod lacus in mi consequat sed</li><li>Nam eu ligula ut massa lobortis scelerisque.</li><li>Curabitur at rhoncus quam.</li></ul></div>
<div class="abs col" style="left:742px;top:680px;width:248px"><h3>Testemonials</h3><div class="quote-box">Curabitur at rhoncus quam. In in tortor quis sem tempor ultricies in eu risus. Fusce posuere justo et metus semper molestie.</div><p style="margin:6px 0 0 30px;color:var(--teal)">Jhon Doe</p></div>
<div class="abs" style="left:954px;top:683px;display:flex;gap:3px"><i style="width:16px;height:16px;background:#c5c9cd;display:block"></i><i style="width:16px;height:16px;background:#c5c9cd;display:block"></i></div>

<div class="abs bar teal" style="top:857px">Meet the team<span class="pair"><i></i><i></i></span></div>
<div class="abs team-card" style="left:210px"><div class="team-photo" role="img" aria-label="Portrait photo of team member" style="background:linear-gradient(#c7b3a2,#5b5e66)"></div><h5>Radek Holmar</h5><small>manager</small></div>
<div class="abs team-card" style="left:411px"><div class="team-photo" role="img" aria-label="Portrait photo of team member" style="background:linear-gradient(#d8cfc2,#8a8f96)"></div><h5>Sanna Corvel</h5><small>client relations</small></div>
<div class="abs team-card" style="left:612px"><div class="team-photo" role="img" aria-label="Portrait photo of team member" style="background:linear-gradient(#b9a591,#6a6e74)"></div><h5>Teodor Vask</h5><small>sales</small></div>
<div class="abs team-card" style="left:810px"><div class="team-photo" role="img" aria-label="Portrait photo of team member" style="background:linear-gradient(#e4e2df,#4d5058)"></div><h5>Liora Brennick</h5><small>office manager</small></div>

<div class="abs bar navy" style="top:1202px">Services<span class="ctrl"></span></div>
<div class="abs service" style="left:205px"><svg width="32" height="28"><path d="M2 2h28v18H12l-7 6v-6H2z" fill="var(--teal)"/></svg><h5>Consulting</h5><p>In quis magna eget magna rutrum hendrerit. Donec dap illus alique.</p></div>
<div class="abs service" style="left:340px"><svg width="30" height="28"><rect x="2" y="2" width="26" height="24" fill="none" stroke="#8a9096" stroke-width="2"/><path d="M2 10h26M2 18h26M11 2v24M19 2v24" stroke="#8a9096" stroke-width="2"/></svg><h5>Planning</h5><p>Curabitur at rhoncus quam. In in tortor quis sem tempor ultricies in.</p></div>
<div class="abs service" style="left:471px"><svg width="34" height="28"><circle cx="12" cy="16" r="8" fill="none" stroke="#8a9096" stroke-width="4" stroke-dasharray="4 2"/><circle cx="26" cy="8" r="5" fill="none" stroke="#8a9096" stroke-width="3" stroke-dasharray="3 2"/></svg><h5>Development</h5><p>Aliquam tellus leo, egestas eget consectetur sed, lobortis vel nisl.</p></div>
<div class="abs service" style="left:604px"><svg width="26" height="28"><path d="M9 2h8M10 2v9L2 26h22L16 11V2" fill="none" stroke="#8a9096" stroke-width="2"/></svg><h5>Production</h5><p>Curabitur at rhoncus quam. In in tortor quis sem tempor ultricies in.</p></div>
<div class="abs service" style="left:737px"><svg width="30" height="28"><rect x="1" y="1" width="28" height="26" fill="none" stroke="#8a9096" stroke-width="2"/><path d="M8 22v-6M13 22v-10M18 22v-7M23 22V7" stroke="#8a9096" stroke-width="3"/></svg><h5>Analysis</h5><p>Curabitur at rhoncus quam. In in tortor quis sem tempor ultricies in.</p></div>
<div class="abs service" style="left:870px"><svg width="30" height="28"><path d="M15 1c2 0 2 3 2 6v4l12 7v3l-12-4v6l4 3v2l-6-2-6 2v-2l4-3v-6L1 21v-3l12-7V7c0-3 0-6 2-6z" fill="#8a9096"/></svg><h5>24 X 7 - Support</h5><p>Curabitur at rhoncus quam. In in tortor quis sem tempor ultricies in.</p></div>

<div class="abs tabs"><span class="on">Extra + Addons</span><span>Tech specs</span><span>Why we are different?</span></div>
<div class="abs tab-body">Sed ut perspiciatis unde omnis iste natus error sit voluptatem accusantium doloremque laudantium, totam rem aperiam, eaque ipsa quae ab illo inventore veritatis et quasi architecto beatae vitae dicta sunt explicabo. Nemo enim ipsam voluptatem quia voluptas sit aspernatur aut odit aut fugit, sed quia consequuntur magni dolores eos qui ratione voluptatem sequi nesciunt. Neque porro quisquam est, qui dolorem ipsum quia dolor sit amet, consectetur, adipisci velit, sed quia non numquam eius modi tempora incidunt ut labore et dolore magnam aliquam quaerat voluptatem. Sed ut perspiciatis unde omnis iste natus error sit voluptatem accusantium doloremque laudantium, totam rem aperiam, eaque ipsa quae ab illo inventore veritatis et quasi architecto beatae vitae dicta sunt explicabo. Nemo enim ipsam voluptatem quia voluptas sit aspernatur aut odit aut fugit, sed quia consequuntur magni dolores eos qui ratione voluptatem sequi nesciunt. Neque porro quisquam est, qui dolorem ipsum quia dolor sit amet, consectetur, adipisci velit.</div>

<div class="abs zone-grey" style="top:1646px;height:507px"></div>
<div class="abs bar teal" style="top:1646px">See our prices and compare!</div>
<div class="abs plan" style="left:210px"><div class="plan-head">Standard</div><div class="plan-price">Free</div><ul><li><i></i>Sed laoreet ullamcorper</li><li><i></i>Smelus semper molestie</li></ul><div class="plan-btn">Sign up for free</div></div>
<div class="abs plan" style="left:411px"><div class="plan-head">Essential</div><div class="plan-price">£2.48<small>*/month</small></div><ul><li><i></i>Sed laoreet ullamcorper</li><li><i></i>Smelus semper molestie</li><li><i></i>Ametus semper molestie</li></ul><div class="plan-btn">Buy now</div></div>
<div class="abs plan featured" style="left:612px"><div class="plan-head">Business Essential</div><div class="plan-price" style="color:var(--teal)">£2.98<small>*/month</small></div><ul><li><i></i>All laoreet ullamcorper</li><li><i></i>Smelus semper molestie</li><li><i></i>Ametus semper molestie</li><li><i></i>Ameus semper molestie</li><li><i></i>Omper molestie</li></ul><div class="plan-btn">Buy now</div></div>
<div class="abs plan" style="left:810px"><div class="plan-head">Business Cloud</div><div class="plan-price">£6.48<small>*/month</small></div><ul><li><i></i>All business options plus</li><li><i></i>Smelus semper molestie</li><li><i></i>Ametus semper molestie</li></ul><div class="plan-btn">Buy now</div></div>

<div class="abs newsletter">
  <div class="abs" style="left:28px;top:26px;width:340px"><h4 style="font-size:13px;color:var(--navy);font-weight:600">Sign up for free</h4><p style="font-size:10px;line-height:13px;color:var(--muted)">Suspendisse dictum quam tortor, et dapibus lacus. Quisque euismod lacus in mi consequat sed pulvinar elit ultricies. Nam eu ligula ut massa</p></div>
  <div class="abs" style="left:402px;top:30px;width:216px;height:40px;background:var(--white);border:1px solid var(--line)"></div>
  <div class="abs" style="left:618px;top:30px;width:140px;height:40px;background:var(--teal);color:var(--white);font-size:9px;font-weight:700;line-height:11px;padding:7px 10px;text-align:center">SUBSCRIBE TO OUR<br><span style="font-size:15px;line-height:17px">NEWSLETTER</span></div>
</div>

<section class="abs map" role="img" aria-label="Street map of the city around the office location with a marker pin"></section>
<div class="abs bar navy" style="top:2155px">Contacts<span class="ctrl"></span></div>

<div class="abs" style="left:210px;top:2507px;font-size:16px;font-weight:600;color:var(--navy)">Contact form</div>
<div class="abs field-box" style="left:210px;top:2551px;width:182px">name</div>
<div class="abs field-box" style="left:210px;top:2597px;width:182px">e-mail</div>
<div class="abs field-box" style="left:210px;top:2643px;width:182px">phone</div>
<div class="abs field-box" style="left:409px;top:2551px;width:380px;height:116px">comment</div>
<div class="abs" style="left:210px;top:2688px;width:176px;height:30px;background:#4b7fbf;color:var(--white);font-size:10px;font-weight:600;display:flex;align-items:center;justify-content:center;gap:6px"><svg width="14" height="12"><path d="M1 1h12v8H5l-3 2V9H1z" fill="#fff"/></svg>Live Chat with Support Now</div>
<div class="abs send" style="left:409px;top:2688px;width:380px;height:42px">SEND</div>

<div class="abs addr" style="left:806px;top:2507px;width:190px">
  <h3 style="font-size:16px;font-weight:600;color:var(--navy);margin-bottom:14px">Address</h3>
  <p style="font-weight:600;color:var(--navy);margin-bottom:6px">Contact Information</p>
  <p style="align-items:flex-start"><svg width="10" height="14"><path d="M5 0a5 5 0 0 1 5 5c0 4-5 9-5 9S0 9 0 5a5 5 0 0 1 5-5z" fill="#8a9096"/></svg><span><b style="color:var(--navy)">Quay Server Lantern</b><br>St. name, Dist. Name, State name,<br>Country Name</span></p>
  <p style="margin-top:6px"><svg width="10" height="12"><rect x="1" y="0" width="8" height="12" rx="1" fill="#8a9096"/></svg>555-310-8826</p>
  <p><svg width="10" height="12"><rect x="1" y="0" width="8" height="12" rx="1" fill="#8a9096"/></svg>555-310-8827</p>
  <p><svg width="10" height="10"><rect width="10" height="8" y="1" fill="#8a9096"/></svg>info@qslantern.uk</p>
</div>
<div class="abs" style="left:806px;top:2708px;display:flex;gap:6px">
  <span role="img" aria-label="Chatterleaf" style="width:24px;height:24px;background:var(--navy);display:block"></span>
  <span role="img" aria-label="Zorbix+" style="width:24px;height:24px;background:var(--teal-dark);display:block"></span>
  <span role="img" aria-label="Murmel" style="width:24px;height:24px;background:var(--teal);display:block"></span>
</div>

<footer class="abs site-footer">© 2015 &nbsp;|&nbsp; <b style="color:var(--white);margin:0 4px">Quay Server Lantern</b> &nbsp;|&nbsp; All Rights Reserved
  <span class="abs" style="right:210px;top:9px;width:18px;height:18px;background:#3d5064"></span></footer>

</body>
</html>
```